依頼詳細
PCとスマホデザインの両方納品をいただきますが、
まずはデザインイメージが確認しやすいPCページのみの提案をお願いします。
スマホページは当選者に納品時にお願いしたいと思います。
スマホサイズは横幅750pxのサイズで作成してください。

レスポンシブウェブデザインを意識したデザインでお願いします。

デザインに関しては、添付してあるデザインレイアウト設計シートを基にお願いします。
参考サイトのURLはデザインレイアウト設計シートに記載してあります。

画像データについては、フリー素材から流用してイメージ画像に当て込んでください。

足りない場合は、一旦他のサイトの写真をサンプルとして入れてください。
また、購入が必要な写真などを利用した場合、価格とサイト名を教えてください。
ページ数
1ページ
希望イメージ
シンプル 複雑
単色 カラフル
暗い 明るい
日常 高級
遊び心 厳粛
未来的 伝統的
女性的 男性的
納品ファイル
• イラストレーター形式 (.ai)
• フォトショップ形式 (.psd)
• PNG形式 (.png)
補足説明
上記のいずれか1つ(アウトラインありとなしの2つ)と高解像度JPGを納品お願いします。

クライアント様より選定いただきました。
一番イメージに近いものでした

ご提案ありがとうございました。
また機会がありましたら是非お願いします。

```html
<!DOCTYPE html>
<html lang="ja">
<head>
<meta charset="utf-8">
<title>株式会社青葉製作所</title>
<link rel="stylesheet" href="https://fonts.googleapis.com/css2?family=Noto+Sans+JP:wght@400;500;700&family=Noto+Serif+JP:wght@400;500;600&family=Cormorant+Garamond:ital,wght@0,400;0,500;1,400&display=swap">
<style>
:root{
  --green:#2f8a3c;
  --green-dark:#256f30;
  --green-light:#3c9a46;
  --ink:#333;
  --muted:#777;
  --line:#ddd;
  --pale:#f4f4f2;
  --white:#fff;
}
*{box-sizing:border-box;margin:0;padding:0}
html,body{width:1200px;height:3224px;overflow:hidden}
body{position:relative;background:var(--white);color:var(--ink);font-family:"Noto Sans JP",sans-serif}
a{text-decoration:none}
.abs{position:absolute}
.serif{font-family:"Noto Serif JP",serif}
.en{font-family:"Cormorant Garamond",serif}

/* header */
.site-header{left:0;top:0;width:1200px;height:56px;display:flex;align-items:center;justify-content:space-between;padding:0 20px 0 24px;background:var(--white)}
.brand{display:flex;align-items:center;gap:10px}
.brand-mark{width:26px;height:26px;background:var(--green)}
.brand-name{font-family:"Noto Serif JP",serif;font-size:15px;font-weight:500;line-height:1.1;color:var(--ink)}
.brand-name small{display:block;font-size:9px;color:var(--muted);font-weight:400}
.global-nav{display:flex;align-items:center;gap:44px;font-size:12px}
.global-nav .current{border-bottom:1px solid var(--ink);padding-bottom:3px}
.btn-contact{background:var(--green);color:var(--white);font-size:12px;padding:9px 26px;border-radius:20px}

/* hero */
.hero{left:0;top:56px;width:1200px;height:764px;background:linear-gradient(180deg,#dfe6ee 0%,#c8d2dc 35%,#8e7c70 58%,#9a9a98 80%,#b9b7b2 100%)}
.hero-sub{left:100px;top:520px;color:var(--white);font-size:22px;font-style:italic;letter-spacing:.05em}
.hero-sub::before{content:"";position:absolute;left:-100px;top:16px;width:92px;height:1px;background:var(--white)}
.hero-title{left:100px;top:568px;color:var(--white);font-size:64px;font-weight:500;letter-spacing:.12em}
.hero-thumbs{right:0;top:760px;display:flex;gap:6px}
.hero-thumbs span{display:block;width:124px;height:60px;background:linear-gradient(135deg,#9fb0c0,#6f7a85)}
.hero-thumbs span:first-child{outline:2px solid var(--white);outline-offset:-2px}

/* about */
.vertical-word{font-family:"Cormorant Garamond",serif;color:#ececec;font-size:120px;writing-mode:vertical-rl;letter-spacing:.06em;line-height:1;z-index:0}
.section-title{width:1200px;left:0;text-align:center;font-family:"Noto Serif JP",serif;font-size:24px;font-weight:500;letter-spacing:.1em}
.section-title::after{content:"";display:block;width:48px;height:1px;background:var(--ink);margin:22px auto 0}
.about-photo{left:620px;top:1060px;width:580px;height:420px;background:linear-gradient(135deg,#c9bba8,#8c7b66 55%,#5f5246)}
.about-lead{left:160px;top:1118px;width:430px;font-family:"Noto Serif JP",serif;font-size:20px;line-height:1.75;letter-spacing:.05em;z-index:1}
.about-text{left:160px;top:1262px;width:430px;font-size:12px;line-height:2;color:#555;z-index:1}
.btn{display:inline-block;background:var(--green);color:var(--white);font-size:12px;text-align:center}
.about-btn{left:160px;top:1406px;width:160px;height:42px;line-height:42px;z-index:2}

/* two panels */
.panel{top:1632px;width:600px;height:408px;display:flex;flex-direction:column;align-items:center;justify-content:center;color:var(--white)}
.panel-products{left:0;background:linear-gradient(160deg,#6e86a2,#4c5d6f 50%,#a89a72)}
.panel-cases{left:600px;background:linear-gradient(160deg,#b9bcbf,#7c8187 55%,#5b5f63)}
.panel h3{font-family:"Noto Serif JP",serif;font-size:26px;font-weight:500;letter-spacing:.1em}
.panel .en{font-size:14px;font-style:italic;margin-top:4px}
.panel .ghost-btn{margin-top:22px;border:1px solid var(--white);font-size:11px;padding:8px 40px}

/* news */
.news-more{left:980px;top:2210px;width:160px;height:38px;line-height:38px;border-radius:20px}
.news-list{left:240px;top:2322px;width:740px;list-style:none}
.news-list li{display:flex;gap:50px;font-size:12px;padding:20px 0;border-bottom:1px solid var(--line)}
.news-list time{color:var(--muted);width:60px}

/* shops */
.shop{top:2780px;width:500px;height:270px;display:flex;align-items:center;padding-left:70px;gap:24px;color:var(--white)}
.shop-official{left:100px;background:var(--green)}
.shop-mall{left:600px;background:var(--green-light)}
.shop-icon{width:56px;height:56px;border-radius:50%;border:2px solid var(--white)}
.shop h3{font-family:"Noto Serif JP",serif;font-size:22px;font-weight:500;letter-spacing:.08em}
.shop .en{font-size:14px;font-style:italic}
.shop svg{position:absolute;right:40px;top:127px}

/* footer */
.site-footer{left:0;top:3100px;width:1200px;height:124px;background:var(--pale)}
.footer-brand{left:100px;top:22px}
.footer-address{left:100px;top:68px;font-size:11px;line-height:1.7;color:#555}
.footer-nav{left:620px;top:26px;display:grid;grid-template-columns:repeat(4,auto);gap:16px 46px;font-size:12px}
.copyright{right:100px;top:82px;font-size:10px;color:var(--muted)}
</style>
</head>
<body>

<header class="site-header abs">
  <div class="brand"><span class="brand-mark"></span><p class="brand-name">株式会社青葉製作所<small>Aoba Mfg. Co., Ltd.</small></p></div>
  <nav class="global-nav">
    <span class="current">事業内容</span><span>製品情報</span><span>採用情報</span><span>会社概要</span>
    <span class="btn-contact">お問い合わせ</span>
  </nav>
</header>

<section class="hero abs" role="img" aria-label="港に積まれたコンテナと上空を飛ぶ貨物機の写真"></section>
<p class="hero-sub abs en">Supporting logistics</p>
<h1 class="hero-title abs serif">物流を、支える。</h1>
<div class="hero-thumbs abs">
  <span role="img" aria-label="倉庫外観の写真"></span><span role="img" aria-label="港湾の写真"></span><span role="img" aria-label="物流センターの写真"></span>
</div>

<p class="vertical-word abs" style="left:20px;top:920px">About</p>
<h2 class="section-title abs" style="top:944px">青葉製作所について</h2>
<p class="about-lead abs">「物流」と「倉庫の収納・保管」の、<br>効率化・安全化を提案します。</p>
<div class="about-photo abs" role="img" aria-label="倉庫で段ボールを運ぶ作業員の写真"></div>
<p class="about-text abs">倉庫の収納・保管スペースを有効に活用し、作業の流れを整えることで物流の効率化を支えています。安全性と使いやすさを両立した製品づくりを通じ、お客様の現場に合わせた最適な提案をお届けします。</p>
<a class="btn about-btn abs">事業内容</a>

<a class="panel panel-products abs" role="img" aria-label="倉庫の棚が並ぶ写真">
  <h3>製品情報</h3><span class="en">Products</span><span class="ghost-btn">製品情報を見る</span>
</a>
<a class="panel panel-cases abs" role="img" aria-label="握手をする手元の写真">
  <h3>導入事例</h3><span class="en">Jirei</span><span class="ghost-btn">導入事例を見る</span>
</a>

<p class="vertical-word abs" style="left:80px;top:2150px">News</p>
<h2 class="section-title abs" style="top:2176px">お知らせ</h2>
<a class="btn news-more abs">一覧へ</a>
<ul class="news-list abs">
  <li><time>2021.00.00</time><span>新製品の情報を掲載しました</span></li>
  <li><time>2021.00.00</time><span>夏季休業日のお知らせ</span></li>
  <li><time>2021.00.00</time><span>導入事例を更新しました</span></li>
</ul>

<a class="shop shop-official abs"><span class="shop-icon"></span><div><h3>公式ショップ</h3><p class="en">Official shop</p></div>
  <svg width="10" height="16" viewBox="0 0 10 16"><path d="M2 1l7 7-7 7" fill="none" stroke="#fff" stroke-width="1.5"/></svg></a>
<a class="shop shop-mall abs"><span class="shop-icon"></span><div><h3>マルシェモール</h3><p class="en">Marche mall</p></div>
  <svg width="10" height="16" viewBox="0 0 10 16"><path d="M2 1l7 7-7 7" fill="none" stroke="#fff" stroke-width="1.5"/></svg></a>

<footer class="site-footer abs">
  <div class="brand footer-brand abs"><span class="brand-mark"></span><p class="brand-name">株式会社青葉製作所<small>Aoba Mfg. Co., Ltd.</small></p></div>
  <p class="footer-address abs">〒000-0000 緑ヶ丘県青葉市中央1丁目2番3号<br>TEL 0000-00-0000 / FAX 0000-00-0001</p>
  <nav class="footer-nav abs"><span>事業内容</span><span>製品情報</span><span>採用情報</span><span>会社概要</span><span>導入事例</span><span>プライバシー</span></nav>
  <p class="copyright abs">Copyright © Aoba Mfg. Co., Ltd.</p>
</footer>

</body>
</html>
```